Corvelle Strategies business card

I need a business card for my new strategic consulting LLC, Corvelle Strategies. We specialize in helping people who care about broadband technology and telecommunications policy, and we're based in Washington DC. I'm looking for a card that says smart, credible, future-facing and signals a high level of expertise. It's DC, so there's clearly a limit to how crazy we can go with this card, but I am looking for a design that reflects a company that is comfortable with technology, policy, and having a little bit fun. I'm uploading my logo below, and I'd like to have it be part of the card design in some fashion.
Target Market(s)
Telecommunications and technology policy professionals
Industry/Entity Type
Technology policy
Contact Information for Business Card
Name of business, my name (Glen Mosswater), email (glen@corvellestrategies-example.com) , phone number (202-555-0148)phone number

```html
<!DOCTYPE html>
<html lang="en">
<head>
<meta charset="UTF-8">
<title>Corvelle Strategies — Business Card</title>
<link rel="stylesheet" href="https://fonts.googleapis.com/css2?family=Inter:wght@400;600&display=swap">
<style>
  :root {
    --backdrop: #5f6b78;
    --brand-blue: #1b4f9a;
    --brand-blue-deep: #123f82;
    --card-paper: #f3f2ee;
    --ink: #1c1c1c;
    --logo-white: #ffffff;
    --sun-amber: #f2a93b;
    --line-grey: #d9d8d3;
  }
  * { margin: 0; padding: 0; box-sizing: border-box; }
  html, body {
    width: 1200px;
    height: 896px;
    overflow: hidden;
    background: var(--backdrop);
    font-family: "Inter", Arial, sans-serif;
  }
  .canvas {
    position: relative;
    width: 1200px;
    height: 896px;
  }
  .card {
    position: absolute;
    left: 342px;
    width: 516px;
  }
  .card-front {
    top: 122px;
    height: 306px;
    background: linear-gradient(160deg, var(--brand-blue) 0%, var(--brand-blue-deep) 100%);
    display: flex;
    align-items: center;
    justify-content: center;
  }
  .wordmark {
    display: flex;
    align-items: center;
    gap: 14px;
  }
  .wordmark-name {
    color: var(--logo-white);
    font-weight: 600;
    font-size: 38px;
    letter-spacing: -0.5px;
  }
  .wordmark-dot {
    width: 24px;
    height: 24px;
    border-radius: 50%;
    background: var(--sun-amber);
  }
  .card-back {
    top: 474px;
    height: 292px;
    background: var(--card-paper);
    overflow: hidden;
  }
  .line-pattern {
    position: absolute;
    right: 0;
    top: 0;
    width: 380px;
    height: 260px;
    background: radial-gradient(ellipse at 80% 55%, var(--line-grey) 0%, rgba(217,216,211,0.35) 45%, rgba(243,242,238,0) 75%);
  }
  .holder-name {
    position: absolute;
    left: 36px;
    top: 120px;
    font-size: 34px;
    font-weight: 400;
    color: var(--ink);
    letter-spacing: -0.3px;
  }
  .contact {
    position: absolute;
    left: 36px;
    top: 190px;
    list-style: none;
    font-size: 18px;
    line-height: 24px;
    color: var(--ink);
  }
</style>
</head>
<body>
  <main class="canvas">
    <section class="card card-front">
      <div class="wordmark">
        <span class="wordmark-name">Corvelle Strategies</span>
        <span class="wordmark-dot"></span>
      </div>
    </section>
    <section class="card card-back">
      <div class="line-pattern" role="img" aria-label="Faint grey decorative pattern of curved circuit-like lines"></div>
      <h1 class="holder-name">Glen Mosswater</h1>
      <ul class="contact">
        <li>Corvelle Strategies</li>
        <li>glen@corvellestrategies-example.com</li>
        <li>202-555-0148</li>
      </ul>
    </section>
  </main>
</body>
</html>
```